Land Buying Company Needs Letterhead for Direct Mail Marketing to Land Owners

We are looking for a professional letterhead that we will be including in our direct mail marketing. We will be sending this to land owners who may be interested in selling or purchasing land.

The letterhead needs to be editable. Headers and footers would look nice, but we are open. We would want it to include our address, website, phone, and email info. For right now the address to use for design purposes would the following:

Address: 415 Bramwell Avenue #600
Dallas, TX 75219
Website - www.quillridgeacres.example
Email - info@quillridgeacres.example
Phone - 866-402-ACRE

I have attached our logo zip file that we just had done on Pixel Guild. Let me know what questions you have, and thank you.

```html
<!DOCTYPE html>
<html lang="en">
<head>
<meta charset="utf-8">
<title>Quillridge Acres Letterhead</title>
<link href="https://fonts.googleapis.com/css2?family=Montserrat:wght@400;600;700&family=Great+Vibes&display=swap" rel="stylesheet">
<style>
  :root {
    --forest: #3f5a1c;
    --leaf: #95c63b;
    --ink: #2a2a2a;
    --paper: #ffffff;
    --backdrop: #efefef;
  }
  * { margin: 0; padding: 0; box-sizing: border-box; }
  html, body {
    width: 714px; height: 1200px; overflow: hidden;
    background: var(--backdrop);
    font-family: "Montserrat", sans-serif;
    color: var(--ink);
  }
  .letterhead {
    position: absolute; left: 12px; top: 112px;
    width: 690px; height: 976px;
    background: var(--paper);
    box-shadow: 0 2px 8px rgba(0,0,0,.18);
    overflow: hidden;
  }
  .brand {
    position: absolute; left: 45px; top: 71px;
    display: flex; align-items: center; gap: 10px;
  }
  .brand-dot {
    width: 45px; height: 45px; border-radius: 50%;
    background: var(--forest);
  }
  .brand-name {
    font-weight: 700; font-size: 24px; letter-spacing: 1px;
    color: var(--leaf);
  }
  .heading { position: absolute; left: 45px; top: 180px; }
  .heading-title {
    font-weight: 700; font-size: 16px; color: var(--forest); letter-spacing: .3px;
  }
  .heading-sub { font-size: 10.5px; margin-top: 2px; }
  .body-copy {
    position: absolute; left: 45px; top: 249px; width: 602px;
    font-size: 10px; line-height: 14px; letter-spacing: -0.1px;
    text-align: justify; hyphens: auto; -webkit-hyphens: auto;
  }
  .body-copy p { margin-bottom: 14px; }
  .sign-off { position: absolute; left: 44px; top: 620px; }
  .sign-name { font-weight: 700; font-size: 12.5px; color: var(--forest); }
  .sign-script {
    font-family: "Great Vibes", cursive; font-size: 17px; margin-top: 4px;
  }
  .contact {
    position: absolute; top: 755px; font-size: 10px; line-height: 12px;
  }
  .contact-left { left: 45px; }
  .contact-right { left: 225px; }
  .contact-item { display: flex; gap: 9px; margin-bottom: 10px; }
  .contact-item svg { width: 10px; height: 10px; flex: none; margin-top: 1px; }
  .phone { font-weight: 700; }
  .footer-band { position: absolute; left: 0; bottom: 0; width: 690px; height: 110px; }
</style>
</head>
<body>
<main class="letterhead" lang="en">
  <div class="brand">
    <div class="brand-dot"></div>
    <div class="brand-name">QUILLRIDGE ACRES</div>
  </div>

  <header class="heading">
    <h1 class="heading-title">LOREM IPSUM</h1>
    <p class="heading-sub">is simply dummy text of the printing</p>
  </header>

  <section class="body-copy">
    <p>It is a long established fact that a reader will be distracted by the readable content of a page when looking at its layout. The point of using Lorem Ipsum is that it has a more-or-less normal distribution of letters, as opposed to using 'Content here, content here', making it look like readable English. Many desktop publishing packages and web page editors now use Lorem Ipsum as their default model text, and a search for 'lorem ipsum' will uncover many web sites still in their infancy. Various versions have evolved over the years, sometimes by accident, sometimes on purpose (injected humour and the like).</p>
    <p>Contrary to popular belief, Lorem Ipsum is not simply random text. It has roots in a piece of classical Latin literature from 45 BC, making it over 2000 years old. Daniel Whitcombe, a Latin professor at Harlow-Brenton College in Virginia, looked up one of the more obscure Latin words, consectetur, from a Lorem Ipsum passage, and going through the cites of the word in classical literature, discovered the undoubtable source. Lorem Ipsum comes from sections 1.10.32 and 1.10.33 of "de Ordine Agrorum et Aquarum" (The Order of Fields and Waters) by Varrin, written in 45 BC.</p>
    <p>There are many variations of passages of Lorem Ipsum available, but the majority have suffered alteration in some form, by injected humour, or randomised words which don't look even slightly believable. If you are going to use a passage of Lorem Ipsum, you need to be sure there isn't anything embarrassing hidden in the middle of text. All the Lorem Ipsum generators on the Internet tend to repeat predefined chunks as necessary, making this the first true generator on the Internet. It uses a dictionary of over 200 Latin words, combined with a handful of model sentence structures, to generate Lorem Ipsum which looks reasonable.</p>
    <p>Lorem Ipsum has been the industry's standard dummy text ever since the 1500s, when an unknown printer took a galley of type and scrambled it to make a type specimen book. It has survived not only five centuries, but also the leap into electronic typesetting, remaining essentially unchanged.</p>
  </section>

  <div class="sign-off">
    <div class="sign-name">LOREM IPSUM</div>
    <div class="sign-script">Is simply dummy</div>
  </div>

  <div class="contact contact-left">
    <div class="contact-item">
      <svg viewBox="0 0 10 10"><path d="M2 0.5 L3.6 2.6 L2.6 3.6 C3.2 5 4.6 6.6 6.4 7.4 L7.4 6.4 L9.5 8 L8.2 9.5 C4.5 9 1 5.5 0.5 1.8 Z" fill="var(--leaf)"/></svg>
      <span class="phone">866-402-ACRE</span>
    </div>
    <div class="contact-item">
      <svg viewBox="0 0 10 10"><path d="M5 0.3 C7.2 0.3 8.6 1.9 8.6 3.8 C8.6 6.3 5 9.7 5 9.7 C5 9.7 1.4 6.3 1.4 3.8 C1.4 1.9 2.8 0.3 5 0.3 Z" fill="var(--leaf)"/><circle cx="5" cy="3.8" r="1.4" fill="#fff"/></svg>
      <span>415 Bramwell Avenue #600<br>Dallas, TX 75219</span>
    </div>
  </div>

  <div class="contact contact-right">
    <div class="contact-item">
      <svg viewBox="0 0 10 10"><rect x="0.5" y="1.8" width="9" height="6.4" fill="var(--leaf)"/><path d="M0.8 2.2 L5 5.4 L9.2 2.2" stroke="#fff" stroke-width="0.8" fill="none"/></svg>
      <span>info@quillridgeacres.example</span>
    </div>
    <div class="contact-item">
      <svg viewBox="0 0 10 10" fill="none" stroke="var(--leaf)" stroke-width="0.9"><circle cx="5" cy="5" r="4.3"/><ellipse cx="5" cy="5" rx="1.9" ry="4.3"/><path d="M0.7 5 H9.3 M1.4 2.8 H8.6 M1.4 7.2 H8.6"/></svg>
      <span>www.quillridgeacres.example</span>
    </div>
  </div>

  <svg class="footer-band" viewBox="0 0 690 110" preserveAspectRatio="none" aria-hidden="true">
    <path d="M0 46 Q345 6 690 26 V110 H0 Z" fill="var(--leaf)"/>
    <path d="M0 58 Q345 20 690 38 V110 H0 Z" fill="var(--forest)"/>
  </svg>
</main>
</body>
</html>
```